Gutschein-Design für Yogalehrerin
Sehr zu empfehlen. Tolle Arbeit. Es hat Spass gemacht. Sehr gerne wieder!
Zielgruppe
Ich bin Yogalehrerin und gebe Online Yoga.
Die Zielgruppe ist: Erwachsene jeden Alters
Aufgabenstellung
Ich benötige einen Gutschein für Privatyoga im Wert von 39 Franken. Die Karte sollte eine weihnachtliche Stimmung mit den Farben Rot / bräunlich / Gold haben. Sie sollte sehr edel aussehen und mit meiner Webseite www.atemfeld.ch übereinstimmen. Die Karte mit Vorder- und Rückseite sollte auch ein Kuvert beinhalten. Auf dem Kuvert sollte in etwa stehen 'Gesundheit für das Neue Jahr' oder dergleichen.

```html
<!DOCTYPE html>
<html lang="de">
<head>
<meta charset="utf-8">
<title>Atemfeld – Gutschein</title>
<link rel="stylesheet" href="https://fonts.googleapis.com/css2?family=Dancing+Script:wght@600;700&family=Fira+Sans+Condensed:wght@300;500;600&family=Roboto:wght@400&display=swap">
<style>
  :root {
    --sheet: #ffffff;
    --card-light: #f4f4f4;
    --card-mid: #dcdcdc;
    --gold: #e6a90e;
    --gold-light: #f8d77a;
    --gold-pale: #fdf3d2;
    --orange: #f18a00;
    --red-orange: #e5411b;
    --ink: #3a3a3a;
    --ink-soft: #555555;
  }
  * { margin: 0; padding: 0; box-sizing: border-box; }
  html, body { width: 791px; height: 1200px; overflow: hidden; background: var(--sheet); }
  body { position: relative; font-family: "Fira Sans Condensed", sans-serif; color: var(--ink); }

  .panel { position: absolute; overflow: hidden;
    background: radial-gradient(ellipse at 62% 45%, var(--card-light) 0%, #ebebeb 55%, var(--card-mid) 100%);
    box-shadow: 0 2px 6px rgba(0,0,0,.12); }
  .panel-label { position: absolute; left: 0; width: 791px; text-align: center;
    font-family: "Roboto", Arial, sans-serif; font-size: 10px; color: #111; }

  .photo { position: absolute; }
  .curve { position: absolute; top: 0; left: 0; }

  .brand { position: absolute; display: flex; flex-direction: column; align-items: center; }
  .brand-dot { border-radius: 50%; border: 2px solid var(--orange); }
  .brand-name { font-weight: 500; color: var(--ink); letter-spacing: 2px; text-transform: uppercase; line-height: 1; }

  .title-script { position: absolute; font-family: "Dancing Script", cursive; font-weight: 700;
    color: var(--gold); text-align: center; white-space: nowrap;
    text-shadow: 0 2px 3px rgba(150,100,0,.25); line-height: 1; }

  /* Front */
  .front { left: 69px; top: 35px; width: 656px; height: 339px; }
  .front .photo { left: 0; top: 0; width: 236px; height: 339px;
    background:
      radial-gradient(ellipse 60% 35% at 25% 78%, rgba(214,58,64,.85) 0%, rgba(214,58,64,0) 100%),
      radial-gradient(ellipse 70% 45% at 55% 30%, rgba(236,160,110,.9) 0%, rgba(236,160,110,0) 100%),
      linear-gradient(170deg, #f3e6d6 0%, #eec7a4 40%, #c9b7ae 70%, #9b9694 100%); }
  .front .brand { left: 283px; width: 356px; top: 38px; gap: 10px; }
  .front .brand-dot { width: 50px; height: 50px; }
  .front .brand-name { font-size: 28px; }
  .front .title-script { left: 270px; width: 380px; top: 148px; font-size: 84px; }
  .voucher-offer { position: absolute; left: 283px; width: 356px; top: 262px; text-align: center;
    font-weight: 500; font-size: 19px; line-height: 24px; color: var(--ink); }

  /* Back */
  .back { left: 69px; top: 415px; width: 656px; height: 339px; }
  .back .portrait { left: 400px; top: 0; width: 256px; height: 339px;
    background:
      radial-gradient(ellipse 45% 50% at 62% 45%, rgba(226,170,140,.95) 0%, rgba(226,170,140,0) 100%),
      radial-gradient(ellipse 70% 70% at 45% 60%, rgba(128,84,58,.85) 0%, rgba(128,84,58,0) 100%),
      linear-gradient(150deg, #f6ead6 0%, #e6cfae 40%, #c79a78 70%, #ece8ef 100%); }
  .round-photo { position: absolute; width: 76px; height: 76px; border-radius: 50%;
    border: 2px solid var(--orange);
    background: radial-gradient(circle at 50% 60%, #7fa9c2 0%, #c9d9e2 55%, #eef2f4 100%); }
  .round-photo.two { background: radial-gradient(circle at 50% 55%, #8c4f3f 0%, #d7b49c 55%, #f3ebe2 100%); }
  .round-photo.three { background: radial-gradient(circle at 50% 55%, #6fa6c4 0%, #e79bb0 35%, #f1f3f5 75%); }
  .back .brand { left: 14px; width: 124px; top: 105px; gap: 6px; }
  .back .brand-dot { width: 38px; height: 38px; }
  .back .brand-name { font-size: 19px; }
  .tagline { position: absolute; left: 14px; width: 124px; top: 177px; text-align: center;
    font-weight: 300; font-size: 19px; color: var(--orange); }
  .pill { position: absolute; border-radius: 16px 0 0 16px;
    background: linear-gradient(90deg, var(--gold-light), var(--gold-pale)); font-weight: 500; color: var(--ink); }
  .info-box { position: absolute; background: #fff; border-radius: 0 0 0 16px;
    border-left: 1px solid var(--gold-light); border-bottom: 1px solid var(--gold-light);
    font-weight: 500; color: var(--ink); }
  .code-label { left: 227px; top: 41px; width: 190px; height: 31px; padding: 6px 14px; font-size: 14px; }
  .code-value { left: 243px; top: 72px; width: 172px; height: 35px; padding: 6px 14px; font-size: 16px; }
  .contact-intro { left: 227px; top: 150px; width: 190px; height: 69px; padding: 8px 14px;
    font-size: 13.5px; line-height: 17px; }
  .contact-list { left: 247px; top: 219px; width: 165px; height: 80px; padding: 10px 12px;
    font-size: 16px; line-height: 20px; list-style: none; }
  .teacher-card { position: absolute; right: 0; bottom: 0; width: 180px; height: 70px;
    background: #fff; border-radius: 70px 0 0 0; text-align: right; padding: 17px 15px 0 0; }
  .teacher-name { font-weight: 600; font-size: 15px; line-height: 20px; color: var(--ink); }
  .teacher-role { font-weight: 300; font-size: 15px; line-height: 20px; color: var(--ink-soft); }

  /* Sticker */
  .sticker { left: 60px; top: 803px; width: 675px; height: 358px; border: 9px solid var(--gold); box-shadow: none; }
  .sticker .photo { left: 0; top: 0; width: 170px; height: 340px;
    background:
      radial-gradient(circle at 40% 28%, rgba(150,140,125,.55) 0%, rgba(150,140,125,0) 30%),
      radial-gradient(circle at 48% 75%, rgba(250,248,244,.9) 0%, rgba(250,248,244,0) 35%),
      linear-gradient(180deg, #e6e3de 0%, #d4cfc6 45%, #e9e7e3 100%); }
  .sticker .title-script { left: 262px; width: 300px; top: 105px; font-size: 70px; }
  .wish { position: absolute; left: 262px; width: 300px; top: 182px; text-align: center;
    font-family: "Dancing Script", cursive; font-weight: 600; font-size: 25px; line-height: 29px; color: var(--ink); }
</style>
</head>
<body>

<section class="panel front">
  <div class="photo" role="img" aria-label="Orchideenblüte und brennendes Teelicht auf Holz"></div>
  <svg class="curve" width="656" height="339" viewBox="0 0 656 339" aria-hidden="true">
    <defs>
      <linearGradient id="band-front" x1="0" y1="0" x2="0" y2="1">
        <stop offset="0" stop-color="#f6b300"/><stop offset="1" stop-color="#e5411b"/>
      </linearGradient>
    </defs>
    <path d="M205 0 L213 0 C252 95 255 240 226 339 L218 339 C244 240 242 95 205 0 Z" fill="#fff" opacity=".55"/>
    <path d="M211 0 L217 0 C268 95 272 240 238 339 L222 339 C252 240 252 95 211 0 Z" fill="url(#band-front)"/>
  </svg>
  <div class="brand"><span class="brand-dot"></span><span class="brand-name">Atemfeld</span></div>
  <h1 class="title-script">Gutschein</h1>
  <p class="voucher-offer">für 1 Online Stunde Privatyoga<br>im Wert von 39 Franken.</p>
</section>
<p class="panel-label" style="top:386px">Vorderseite</p>

<section class="panel back">
  <div class="photo portrait" role="img" aria-label="Porträtfoto der Yogalehrerin"></div>
  <svg class="curve" width="656" height="339" viewBox="0 0 656 339" aria-hidden="true">
    <defs>
      <linearGradient id="arc-back" x1="0" y1="0" x2="0" y2="1">
        <stop offset="0" stop-color="#f6b300"/><stop offset="1" stop-color="#e5411b"/>
      </linearGradient>
    </defs>
    <path d="M91 0 C190 60 240 230 91 339" fill="none" stroke="url(#arc-back)" stroke-width="1.5"/>
    <path d="M420 0 L428 0 C444 95 440 240 408 339 L400 339 C430 240 432 95 420 0 Z" fill="#fff" opacity=".7"/>
    <path d="M410 0 L418 0 C438 95 432 240 398 339 L386 339 C420 240 426 95 410 0 Z" fill="url(#arc-back)"/>
  </svg>
  <div class="round-photo one" style="left:112px;top:30px" role="img" aria-label="Frau meditiert im Schneidersitz"></div>
  <div class="round-photo two" style="left:141px;top:130px" role="img" aria-label="Mann in Meditationshaltung"></div>
  <div class="round-photo three" style="left:112px;top:230px" role="img" aria-label="Zwei Personen in Kriegerhaltung"></div>
  <div class="brand"><span class="brand-dot"></span><span class="brand-name">Atemfeld</span></div>
  <p class="tagline">Yoga für Alle.</p>

  <p class="pill code-label">Gutscheincode:</p>
  <p class="info-box code-value">ATEMFELD-5RD3</p>
  <p class="pill contact-intro">Ich freue mich auf unsere<br>gemeinsame Yogastunde<br>und bin erreichbar unter:</p>
  <ul class="info-box contact-list">
    <li>079 318 42 67</li>
    <li>mirjam@atemfeld.ch</li>
    <li>www.atemfeld.ch</li>
  </ul>

  <div class="teacher-card">
    <p class="teacher-name">Mirjam Keller</p>
    <p class="teacher-role">zertifizierte Yogalehrerin</p>
  </div>
</section>
<p class="panel-label" style="top:768px">Rückseite</p>

<section class="panel sticker">
  <div class="photo" role="img" aria-label="Hängende silberne Weihnachtskugeln"></div>
  <h2 class="title-script">Gesundheit</h2>
  <p class="wish">für das neue Jahr<br>wünscht Reto Baumann!</p>
</section>
<p class="panel-label" style="top:1176px">Aufkleber</p>

</body>
</html>
```